Business card for law firm

Need business card for new law firm. Think confident, authoritative, conservative, but not stuffy or old-fashioned.

Contact Information for Business Card

Content for card - logo (uploaded), plus the following:

Paul Wexbury (larger font)
Managing Partner (larger font, but not as large as name)
Level 9, 41 Tansy Lane
Sydney NSW 2000
Main Tel 02 7346 2190
Direct Tel 02 6273 4415
Email paul@qvlegal.com.au
www.qvlegal.com.au

Letterhead design should include logo plus:
Level 9, 41 Tansy Lane
Sydney NSW 2000
Tel 02 6273 4415
www.qvlegal.com.au

```html
<!DOCTYPE html>
<html lang="en">
<head>
<meta charset="utf-8">
<title>Quillvale Legal — Business Card</title>
<link rel="stylesheet" href="https://fonts.googleapis.com/css2?family=Cinzel:wght@500&family=Open+Sans:wght@400;700&display=swap">
<style>
  :root {
    --navy: #0e1f57;
    --ink: #141414;
    --text: #2b2b2b;
    --rule: #b9b9b9;
    --paper: #ffffff;
    --backdrop: #dcdcde;
  }
  * { box-sizing: border-box; margin: 0; padding: 0; }
  html, body {
    width: 1200px; height: 1082px; overflow: hidden;
    background: var(--backdrop);
    font-family: "Open Sans", Arial, sans-serif;
  }
  .card {
    position: absolute;
    width: 801px; height: 458px;
    overflow: hidden;
  }
  .card--front {
    left: 325px; top: 68px;
    background: var(--paper);
    border: 1px solid #c9c9c9;
  }
  .card--back {
    left: 64px; top: 568px;
    background: var(--navy);
  }

  /* Front */
  .brand {
    position: absolute; left: 40px; width: 390px; top: 95px;
    display: flex; flex-direction: column; align-items: center;
  }
  .brand__mark {
    width: 74px; height: 74px; background: var(--navy);
    margin-bottom: 40px;
  }
  .brand__name {
    font-family: "Cinzel", "Times New Roman", serif;
    font-weight: 500; font-size: 31px; letter-spacing: 1px;
    color: var(--ink); white-space: nowrap;
  }
  .divider {
    position: absolute; left: 448px; top: 84px;
    width: 1px; height: 255px; background: var(--rule);
  }
  .contact {
    position: absolute; left: 472px; top: 82px;
    color: var(--text);
  }
  .contact__name {
    font-size: 25px; font-weight: 700; color: var(--navy);
    text-transform: uppercase; line-height: 1.2;
  }
  .contact__title {
    font-size: 19px; text-transform: uppercase; line-height: 1.3;
    margin-bottom: 14px;
  }
  .contact__address { font-size: 20px; line-height: 29px; margin-bottom: 8px; }
  .contact__list { list-style: none; font-size: 20px; line-height: 31px; }
  .contact__list li { display: flex; align-items: center; gap: 6px; }
  .contact__list svg { width: 16px; height: 16px; flex: none; }

  .wave { position: absolute; left: 0; top: 0; width: 801px; height: 458px; }

  /* Back */
  .back__brand {
    position: absolute; left: 0; right: 0; top: 120px;
    display: flex; flex-direction: column; align-items: center;
  }
  .back__mark { width: 100px; height: 100px; background: var(--paper); margin-bottom: 36px; }
  .back__name {
    font-family: "Cinzel", "Times New Roman", serif;
    font-weight: 500; font-size: 40px; color: var(--paper); letter-spacing: 1px;
  }
  .back__web {
    position: absolute; left: 0; right: 0; top: 390px;
    text-align: center; color: var(--paper);
    font-size: 19px; letter-spacing: 3px;
  }
</style>
</head>
<body>

<section class="card card--front">
  <svg class="wave" viewBox="0 0 801 458" aria-hidden="true">
    <path fill="var(--navy)" d="M0,398 C150,455 300,445 450,424 C600,403 720,424 801,442 L801,458 L0,458 Z"/>
    <path fill="var(--ink)" d="M0,352 C120,402 260,422 420,406 C600,388 720,418 801,437 C720,424 600,398 430,414 C270,430 130,430 0,388 Z"/>
  </svg>

  <div class="brand">
    <div class="brand__mark"></div>
    <div class="brand__name">QUILLVALE LEGAL</div>
  </div>

  <div class="divider"></div>

  <div class="contact">
    <div class="contact__name">Paul Wexbury</div>
    <div class="contact__title">Managing Partner</div>
    <div class="contact__address">Level 9, 41 Tansy Lane<br>Sydney NSW 2000</div>
    <ul class="contact__list">
      <li>
        <svg viewBox="0 0 16 16"><circle cx="8" cy="8" r="7" fill="none" stroke="var(--navy)" stroke-width="1.5"/><path d="M5.5 4.5 L7 6 L6.2 7 C6.8 8.3 7.7 9.2 9 9.8 L10 9 L11.5 10.5 L10.5 11.6 C7.5 11 5 8.5 4.4 5.5 Z" fill="var(--navy)"/></svg>
        02 7346 2190 (Main)
      </li>
      <li>
        <svg viewBox="0 0 16 16"><circle cx="8" cy="8" r="7" fill="none" stroke="var(--navy)" stroke-width="1.5"/><path d="M5.5 4.5 L7 6 L6.2 7 C6.8 8.3 7.7 9.2 9 9.8 L10 9 L11.5 10.5 L10.5 11.6 C7.5 11 5 8.5 4.4 5.5 Z" fill="var(--navy)"/></svg>
        02 6273 4415 (Direct)
      </li>
      <li>
        <svg viewBox="0 0 16 16"><rect x="1.5" y="4" width="13" height="9" rx="1" fill="var(--navy)"/><path d="M1.5 4.5 L8 9 L14.5 4.5" fill="none" stroke="#fff" stroke-width="1.2"/></svg>
        paul@qvlegal.com.au
      </li>
      <li>
        <svg viewBox="0 0 16 16" fill="none" stroke="var(--navy)" stroke-width="1.3"><circle cx="8" cy="8" r="6.5"/><ellipse cx="8" cy="8" rx="3" ry="6.5"/><path d="M1.5 8 H14.5 M2.5 5 H13.5 M2.5 11 H13.5"/></svg>
        www.qvlegal.com.au
      </li>
    </ul>
  </div>
</section>

<section class="card card--back">
  <div class="back__brand">
    <div class="back__mark"></div>
    <div class="back__name">QUILLVALE LEGAL</div>
  </div>
  <div class="back__web">www.qvlegal.com.au</div>
</section>

</body>
</html>
```